LustPrep.com 350x250 Creative Banner Ad & Logo **

UPDATE: For inspiration, please see new images attached. Also, please visit the following link to understand what our website niche will be about:

https://m.vidhollow.example/watch?v=Qk3TpaLx8Rn&feature=vidhol.example

We need several creative banner ad's (350x250) for various PornSites based on 3 themes; gay, straight and multiracial. Winning designers should have proven record of successful clickthrough conversions. Our website; LustPrep.com will offer 20,000 adult novelty products, BUT we want to position ourselves as the go to provider for premium Grooming and Shaving products - hence the name LustPrep.... We also need a new Logo for our website and other marketing materials (see attached). Unfortunately, this is the best we could do on our own and does not at this point represent the brand image we are looking for. We are looking for more creative ideas..

Target Market(s)

Adult Males 80%, Adult Females 20%

Logo Text

LustPrep.com - Set for Whatever!

Requirements
Must have
• From designer with proven track record of high click through success rates. Designs should be creative and help establish a brand image. Three (3) themes; gay, straight, multiracial. We are open to suggestions. Ads will be displayed on the big 3 porn sites through velvet routing - so must be in .jpg format and compatable with all devices.
Nice to have
• Multiple design options
New and creative ideas
Should not have
• We are paying for custom design service and do not want anything that looks and feels like a standard template or "off-the-shelf" design.. We expect to be "Wowed!".

```html
<!DOCTYPE html>
<html lang="en">
<head>
<meta charset="utf-8">
<title>LustPrep – Grooming Banner</title>
<link href="https://fonts.googleapis.com/css2?family=Pacifico&family=Montserrat:wght@400;600;800&display=swap" rel="stylesheet">
<style>
  :root {
    --purple-deep: #7a1f8f;
    --purple-mid: #9b3ab0;
    --purple-light: #c06ad0;
    --plum: #8e2a6e;
    --yellow: #f4d21c;
    --white: #ffffff;
    --ink: #3a3a3a;
    --skin-light: #e8cbb8;
    --skin-mid: #cfa48c;
  }
  html, body {
    margin: 0;
    padding: 0;
    width: 1200px;
    height: 1200px;
    overflow: hidden;
    background: var(--white);
  }
  .banner {
    position: relative;
    width: 1200px;
    height: 1200px;
    overflow: hidden;
    background: radial-gradient(circle at 45% 30%, var(--purple-light) 0%, var(--purple-mid) 35%, var(--purple-deep) 100%);
    font-family: 'Montserrat', sans-serif;
  }
  .product-photo {
    position: absolute;
    left: 300px;
    top: 380px;
    width: 900px;
    height: 700px;
    background: radial-gradient(ellipse at 75% 55%, var(--skin-light) 0%, var(--skin-mid) 40%, rgba(207,164,140,0) 75%);
  }
  .headline {
    position: absolute;
    left: 0;
    width: 1130px;
    text-align: center;
    margin: 0;
    color: var(--white);
    font-family: 'Pacifico', cursive;
    font-weight: 400;
    line-height: 1;
  }
  .headline--great { top: 92px; font-size: 132px; left: 10px; }
  .headline--sub { top: 268px; font-size: 92px; }
  .ghost-title {
    position: absolute;
    left: 0;
    top: 700px;
    width: 1200px;
    text-align: center;
    font-family: 'Pacifico', cursive;
    font-size: 104px;
    line-height: 1;
    letter-spacing: 6px;
    color: transparent;
    -webkit-text-stroke: 1.5px rgba(255,255,255,0.35);
    white-space: nowrap;
  }
  .deco { position: absolute; left: 0; top: 0; }
  .sale-badge {
    position: absolute;
    left: 912px;
    top: 220px;
    width: 252px;
    text-align: center;
    color: var(--white);
    font-weight: 800;
  }
  .sale-badge__label { font-size: 23px; letter-spacing: 0.5px; }
  .sale-badge__value { font-size: 52px; color: var(--yellow); line-height: 1.1; letter-spacing: -1px; }
  .brand-name {
    position: absolute;
    left: 96px;
    top: 1036px;
    margin: 0;
    font-size: 58px;
    font-weight: 800;
    color: var(--purple-mid);
    letter-spacing: 1px;
  }
  .cta-button {
    position: absolute;
    left: 540px;
    top: 1096px;
    width: 192px;
    height: 48px;
    border-radius: 24px;
    background: var(--plum);
    color: var(--white);
    font-size: 16px;
    font-weight: 600;
    display: flex;
    align-items: center;
    justify-content: center;
    letter-spacing: 0.5px;
  }
  .divider {
    position: absolute;
    left: 798px;
    top: 1062px;
    width: 2px;
    height: 90px;
    background: var(--ink);
  }
  .tagline {
    position: absolute;
    left: 840px;
    top: 1074px;
    margin: 0;
    font-size: 18px;
    line-height: 26px;
    color: var(--ink);
    letter-spacing: 0.5px;
  }
  .tagline strong { font-weight: 600; }
</style>
</head>
<body>
<div class="banner">
  <div class="product-photo" role="img" aria-label="Photo of a hand using a black electric trimmer on skin"></div>

  <div class="ghost-title">HAIR SHAVE PUBS</div>

  <svg class="deco" width="1200" height="1200" viewBox="0 0 1200 1200" aria-hidden="true">
    <!-- bottom wave -->
    <path d="M0,935 C150,875 320,855 480,875 C700,905 900,1005 1200,1015 L1200,1200 L0,1200 Z" fill="var(--yellow)"/>
    <path d="M0,962 C150,902 320,882 480,902 C700,932 900,1030 1200,1040 L1200,1200 L0,1200 Z" fill="var(--white)"/>
    <!-- dashed arrow -->
    <path d="M268,566 C210,540 170,500 200,460 C225,430 190,410 175,440 C160,470 190,400 232,364" fill="none" stroke="var(--white)" stroke-width="2" stroke-dasharray="7 6"/>
    <path d="M212,352 L248,350 L232,380 Z" fill="var(--yellow)"/>
    <!-- sale cloud -->
    <path d="M940,300 C900,300 900,250 940,245 C930,205 985,185 1010,210 C1030,180 1090,185 1095,220 C1140,210 1165,255 1140,280 C1165,305 1140,350 1100,340 C1085,375 1030,375 1015,350 C990,375 935,360 945,330 C920,330 915,305 940,300 Z" fill="none" stroke="var(--yellow)" stroke-width="3"/>
    <circle cx="958" cy="376" r="9" fill="none" stroke="var(--yellow)" stroke-width="2.5"/>
    <circle cx="936" cy="396" r="5" fill="none" stroke="var(--yellow)" stroke-width="2"/>
    <circle cx="920" cy="408" r="3" fill="none" stroke="var(--yellow)" stroke-width="1.5"/>
  </svg>

  <h1 class="headline headline--great">Great</h1>
  <h2 class="headline headline--sub">hair shave pubs</h2>

  <div class="sale-badge">
    <div class="sale-badge__label">SAVE UPTO</div>
    <div class="sale-badge__value">50%</div>
  </div>

  <p class="brand-name">LustPrep</p>
  <div class="cta-button">ORDER NOW</div>
  <div class="divider"></div>
  <p class="tagline">LOREM IPSUM<br>DOLOR SIT<br><strong>CONS CTETUR</strong></p>
</div>
</body>
</html>
```